Elderwell Solutions company needs a homepage design

We need a homepage designed for a new company based in Des Moines, IA called Go Elderwell Solutions. They sell Elderwell Supplement plans to seniors. The design should communicate trust, security, be vibrant and easy to read with larger font and clear messages. The goal for visitors is to ultimately get a free quote and purchase a plan after a call from a licensed agent.

Industry/Entity Type

It Company

```html
<!DOCTYPE html>
<html lang="en">
<head>
<meta charset="utf-8">
<title>Go Elderwell Solutions</title>
<link href="https://fonts.googleapis.com/css2?family=Open+Sans:ital,wght@0,400;0,600;0,700;1,400&family=Montserrat:wght@500;600;700&display=swap" rel="stylesheet">
<style>
:root{
  --topbar:#3b3b3b;
  --nav:#5b5b5b;
  --olive:#6b8a2c;
  --green-1:#9cc23c;
  --green-2:#8cb536;
  --green-3:#7b9f37;
  --green-4:#6a8a34;
  --sage:#a5cf95;
  --sage-dark:#7fb06e;
  --red:#e0493b;
  --ink:#333333;
  --muted:#777777;
  --purple:#6a3f8f;
  --section-gray:#f6f5f2;
  --quote-gray:#efeeec;
  --footer:#2e2e2e;
  --footer-bottom:#1b1b1b;
  --white:#ffffff;
}
*{margin:0;padding:0;box-sizing:border-box}
html,body{width:1200px;height:3579px;overflow:hidden}
body{position:relative;font-family:"Open Sans",Arial,sans-serif;color:var(--ink);background:var(--white)}
.abs{position:absolute}

/* top bar */
.topbar{left:0;top:0;width:1200px;height:33px;background:var(--topbar);color:#ddd;font-size:12px}
.topbar .contact{left:67px;top:9px;display:flex;gap:40px;align-items:center}
.topbar .contact span{display:flex;align-items:center;gap:8px}
.topbar .social{right:72px;top:11px;display:flex;gap:12px;align-items:center}
.topbar .social i{display:block;width:11px;height:11px;border-radius:50%;background:#cfcfcf}
.topbar .social .user{margin-right:14px;display:flex}

/* header */
.site-header{left:0;top:33px;width:1200px;height:105px;background:var(--white)}
.brand{left:67px;top:30px;display:flex;align-items:center;gap:12px;font-size:30px;font-weight:600;color:var(--olive)}
.brand-mark{width:16px;height:16px;background:var(--olive)}
.join{left:938px;top:29px;width:188px;height:48px;background:var(--olive);color:#fff;font-family:"Montserrat",sans-serif;font-weight:600;font-size:18px;letter-spacing:1px;display:flex;align-items:center;justify-content:center;border-radius:2px}

/* nav */
.main-nav{left:0;top:138px;width:1200px;height:43px;background:var(--nav)}
.main-nav a{position:absolute;top:12px;color:#fff;font-family:"Montserrat",sans-serif;font-size:15px;font-weight:500;letter-spacing:.5px;text-decoration:none}
.main-nav .search{position:absolute;left:1100px;top:8px}

/* hero */
.hero{left:0;top:181px;width:1200px;height:451px;background:linear-gradient(90deg,#7a7570 0%,#a59e95 30%,#c9bfb3 55%,#8b7a6a 80%,#5e5a4f 100%)}
.hero-title{left:62px;top:152px;color:#fff;font-size:45px;line-height:62px;font-weight:400}
.hero-arrow{top:210px;color:rgba(255,255,255,.8);font-size:30px}

/* feature strip */
.features{left:67px;top:563px;width:1064px;height:227px;display:flex}
.feature{flex:1;padding:30px 25px;color:#fff}
.feature h3{font-family:"Montserrat",sans-serif;font-size:15px;font-weight:600;margin-bottom:12px}
.feature p{font-size:12px;line-height:20px;font-weight:600}
.feature .btn{display:inline-block;margin-top:16px;border:2px solid #fff;padding:8px 22px;font-family:"Montserrat",sans-serif;font-size:11px;font-weight:700;letter-spacing:1px}
.f1{background:var(--green-1)}.f2{background:var(--green-2)}.f3{background:var(--green-3)}.f4{background:var(--green-4)}

/* vision */
.vision-eyebrow{left:0;top:841px;width:1200px;text-align:center;font-size:22px;color:#555;letter-spacing:.5px}
.vision-title{left:0;top:876px;width:1200px;text-align:center;font-size:34px;font-weight:400;color:var(--ink)}
.stat{width:340px;text-align:center}
.stat b{display:block;font-weight:400;font-size:38px;color:var(--red);margin-bottom:20px}
.stat p{font-size:15px;line-height:22px;color:var(--muted)}

/* gray section */
.panels-bg{left:0;top:1169px;width:1200px;height:1062px;background:var(--section-gray)}
.panel{position:absolute}
.panel h4{font-size:21px;font-weight:600;color:var(--ink);margin-bottom:16px}
.panel p{font-size:16px;line-height:25px;color:#666}
.btn-outline{display:inline-block;font-family:"Montserrat",sans-serif;font-size:14px;font-weight:600;letter-spacing:1.5px;text-align:center;padding:10px 0}
.green-block{left:112px;top:1226px;width:480px;height:635px;background:var(--sage);padding:55px 62px}
.green-block h4{color:#3d3d3d}
.green-block p{color:#5a6b55}
.green-block .btn-outline{background:#fff;color:var(--sage-dark);width:180px;margin-top:30px}
.team{display:flex;gap:6px;margin-top:36px}
.team span{width:82px;height:82px;border-radius:50%;border:3px solid #fff;background:linear-gradient(135deg,#c9a88a,#6d5a4a)}
.team-note{margin-top:42px;border-left:3px solid #fff;padding-left:18px}
.white-top{left:597px;top:1226px;width:489px;height:318px;background:#fff;padding:55px 70px}
.white-top .btn-outline{border:3px solid var(--sage);color:var(--sage-dark);width:310px;margin-top:26px;border-radius:3px}
.photo{left:602px;top:1544px;width:484px;height:317px;background:linear-gradient(160deg,#c9d7a8 0%,#d8bba4 45%,#b49a85 70%,#7d8a5a 100%)}
.insurance{left:112px;top:1861px;width:480px;height:306px;background:#fff;padding:40px 58px}
.insurance h4,.labs h4{font-size:23px;font-weight:400;margin-bottom:14px}
.insurance p,.labs p{font-size:15px;line-height:22px;color:#444}
.insurance .btn-outline{border:3px solid #7bb160;color:#4e7f3a;width:140px;margin-top:22px;font-size:12px;padding:8px 0}
.insurance a{display:block;color:var(--purple);font-size:15px;font-weight:600;margin-top:12px;text-decoration:none}
.labs{left:602px;top:1861px;width:484px;height:306px;background:var(--sage);padding:40px 64px}
.labs h4{color:#333}
.labs a{color:var(--purple);font-weight:600;text-decoration:none}
.labs .btn-outline{background:#fff;border:2px solid #4e7f3a;color:#4e7f3a;width:312px;margin-top:24px;font-size:12px;padding:8px 0}

/* membership */
.membership-title{left:0;top:2285px;width:1200px;text-align:center;font-size:35px;font-weight:400;color:var(--ink)}
.promise{width:510px}
.promise .head{display:flex;align-items:center;gap:26px;height:72px}
.promise h5{font-size:35px;font-weight:400;color:#777}
.promise p{font-size:21px;line-height:34px;color:#444;margin-top:12px}

/* testimonial */
.testimonial{left:0;top:2622px;width:1200px;height:432px;background:var(--quote-gray);text-align:center}
.avatar{left:540px;top:62px;width:120px;height:120px;border-radius:50%;border:4px solid #fff;background:linear-gradient(135deg,#e0b98c,#a77a52)}
.quote{left:0;top:195px;width:1200px;font-style:italic;font-size:22px;line-height:31px;color:#555}
.quote-author{left:0;top:296px;width:1200px;padding-left:225px;font-size:21px;font-weight:600;color:#222}
.dots{left:576px;top:361px;display:flex;gap:12px}
.dots i{width:8px;height:8px;border-radius:50%;background:#9fd08c}
.dots i.on{background:#6aaa52}

/* footer */
.site-footer{left:0;top:3054px;width:1200px;height:446px;background:var(--footer);color:#ddd}
.foot-col{position:absolute;top:66px}
.foot-col h6{font-size:20px;font-weight:700;color:#fff;letter-spacing:.5px;margin-bottom:24px}
.foot-col li{list-style:none;font-size:17px;line-height:31px}
.foot-col.story li{line-height:40px}
.copyright{left:0;top:3500px;width:1200px;height:79px;background:var(--footer-bottom);color:#ddd;font-size:13px;text-align:center;line-height:79px}
</style>
</head>
<body>

<div class="abs topbar">
  <div class="abs contact">
    <span><svg width="12" height="12" viewBox="0 0 24 24"><path fill="#ddd" d="M6.6 10.8a15 15 0 006.6 6.6l2.2-2.2a1 1 0 011-.25 11 11 0 003.6.57 1 1 0 011 1V20a1 1 0 01-1 1A17 17 0 013 4a1 1 0 011-1h3.5a1 1 0 011 1c0 1.25.2 2.45.57 3.57a1 1 0 01-.25 1z"/></svg>Call us: 555-010-2040</span>
    <span><svg width="13" height="10" viewBox="0 0 26 20"><rect x="1" y="1" width="24" height="18" fill="none" stroke="#ddd" stroke-width="2"/><path d="M1 1l12 10 12-10" fill="none" stroke="#ddd" stroke-width="2"/></svg>Email: hello@elderwell-mail.com</span>
  </div>
  <div class="abs social">
    <span class="user"><svg width="12" height="12" viewBox="0 0 24 24"><circle cx="12" cy="7" r="5" fill="#ddd"/><path d="M2 24c0-6 5-9 10-9s10 3 10 9z" fill="#ddd"/></svg></span>
    <i></i><i></i><i></i><i></i><i></i><i></i>
  </div>
</div>

<header class="abs site-header">
  <div class="abs brand"><span class="brand-mark"></span>Go Elderwell Solutions</div>
  <div class="abs join">JOIN TODAY</div>
</header>

<nav class="abs main-nav">
  <a style="left:72px">WHAT WE DO</a>
  <a style="left:239px">PRIMARY CARE TEAM</a>
  <a style="left:468px">LOCATIONS</a>
  <a style="left:623px">INSURANCE</a>
  <a style="left:783px">MEMBERSHIP</a>
  <svg class="search" width="26" height="26" viewBox="0 0 24 24"><circle cx="10" cy="10" r="6.5" fill="none" stroke="#fff" stroke-width="2"/><path d="M15 15l6 6" stroke="#fff" stroke-width="2.4"/></svg>
</nav>

<section class="abs hero" role="img" aria-label="Photo of a woman choosing fresh vegetables at a market">
  <h1 class="abs hero-title">Lorem ipsum dolor sit amet<br>&nbsp;consectetur adipiscing</h1>
  <span class="abs hero-arrow" style="left:55px">&#8249;</span>
  <span class="abs hero-arrow" style="left:1120px">&#8250;</span>
</section>

<div class="abs features">
  <div class="feature f1"><h3>Professional staff</h3><p>Lorem ipsum dolor sit amet, consectetur adipiscing elit. Aliquam quis semper felis.</p><span class="btn">READ MORE</span></div>
  <div class="feature f2"><h3>Affordable prices</h3><p>Aliquam sit amet porttitor ex, sit amet pellentesque nibh. Praesent viverra dui augue.</p><span class="btn">VIEW PRICELIST</span></div>
  <div class="feature f3"><h3>Insurance partners</h3><p>Praesent cursus ligula elit, vitae ullamcorper felis sodales non. Suspendisse ut hendrerit.</p><span class="btn">READ MORE</span></div>
  <div class="feature f4"><h3>Consult our doctors</h3><p>Select the doctor you prefer and book a visit with him or her in a matter of minutes.</p><span class="btn">CHOOSE A DOCTOR &#8964;</span></div>
</div>

<div class="abs vision-eyebrow">OUR VISION</div>
<h2 class="abs vision-title">A Completely Different Approach</h2>
<div class="abs stat" style="left:62px;top:958px"><b>95%</b><p>Lorem ipsum dolor sit amet, consectetur adipiscing elit. Praesent eget tortor condimentum accumsan libero at euismod risus.</p></div>
<div class="abs stat" style="left:431px;top:958px"><b>Today</b><p>Lorem ipsum dolor sit amet, consectetur adipiscing elit. Praesent eget tortor condimentum accumsan libero at euismod risus.</p></div>
<div class="abs stat" style="left:803px;top:958px"><b>24/7</b><p>Lorem ipsum dolor sit amet, consectetur adipiscing elit. Praesent eget tortor condimentum accumsan libero at euismod risus.</p></div>

<div class="abs panels-bg"></div>
<div class="panel green-block">
  <h4>Lorem ipsum dolor sit a</h4>
  <p>Lorem ipsum dolor sit amet, consectetur ad ipiscing elit. Praesent eget tortor condimen tum, accumsan libero at, euismod risus.</p>
  <span class="btn-outline">LEARN NOW</span>
  <div class="team" role="img" aria-label="Portraits of four care team members"><span></span><span></span><span></span><span></span></div>
  <div class="team-note"><h4>Lorem ipsum</h4><p>Lorem ipsum dolor sit amet, consectetur ad ipiscing elit. Praesent eget tortor condimen tum, accumsan libero at, euismod risus.</p></div>
</div>
<div class="panel white-top">
  <h4 style="font-weight:400">Lorem ipsum dolor sit a</h4>
  <p>Lorem ipsum dolor sit amet, consectetur ad ipiscing elit. Praesent eget tortor condimen tum, accumsan libero at, euismod risus.</p>
  <span class="btn-outline">LEARN NOW</span>
</div>
<div class="panel photo" role="img" aria-label="Photo of a smiling grandparent couple with their granddaughter outdoors"></div>
<div class="panel insurance">
  <h4>We Accept Your Health Insurance</h4>
  <p>Oak Clinic accepts health plans from most insurance carriers and Elderwell. Our goal is to make quality health care accessible to everyone.</p>
  <span class="btn-outline">VIEW PLANS</span>
  <a>How insurance works at Oak Clinic</a>
  <a style="margin-top:6px">How we work with ACA plans</a>
</div>
<div class="panel labs">
  <h4>On-Site Labs</h4>
  <p>We offer <a>lab and blood tests</a> on a walk-in basis to help remove the hassle out of getting your lab work done. No appointments are necessary, but hours vary by office.</p>
  <span class="btn-outline">CHECK NEARBY LAB HOURS</span>
</div>

<h2 class="abs membership-title">Risk-Free Membership</h2>
<div class="abs promise" style="left:67px;top:2360px">
  <div class="head">
    <svg width="58" height="68" viewBox="0 0 58 68"><rect x="4" y="8" width="50" height="57" rx="3" fill="none" stroke="var(--purple)" stroke-width="3"/><rect x="18" y="2" width="22" height="12" rx="2" fill="#fff" stroke="var(--purple)" stroke-width="3"/><path d="M29 22v14M22 29h14" stroke="var(--purple)" stroke-width="3"/><path d="M14 46h30M14 54h30" stroke="var(--purple)" stroke-width="2.5"/></svg>
    <h5>Affordable Care</h5>
  </div>
  <p>Lorem ipsum dolor sit amet, consectetur ad ipiscing elit. Praesent eget tortor condimen tum, accumsan libero at, euismod risus.</p>
</div>
<div class="abs promise" style="left:625px;top:2360px">
  <div class="head">
    <svg width="52" height="68" viewBox="0 0 52 68"><path d="M14 36l-6 28 18-9 18 9-6-28" fill="none" stroke="var(--purple)" stroke-width="3"/><circle cx="26" cy="24" r="20" fill="#fff" stroke="var(--purple)" stroke-width="3"/><path d="M26 12l3.5 7.5 8 1-6 5.5 1.6 8-7.1-4-7.1 4 1.6-8-6-5.5 8-1z" fill="var(--purple)"/></svg>
    <h5>The Oak Clinic Promise</h5>
  </div>
  <p>Lorem ipsum dolor sit amet, consectetur ad ipiscing elit. Praesent eget tortor condimen tum, accumsan libero at, euismod risus.</p>
</div>

<section class="abs testimonial">
  <div class="abs avatar" role="img" aria-label="Portrait of the reviewing client"></div>
  <p class="abs quote">Lorem ipsum dolor sit amet, consectetur adipiscing elit Praesent eget tortor<br>condimentum accumsan libero at euismod risus<br>Aenean a cursus ex, bibendum</p>
  <div class="abs quote-author">- DANA LOWELL</div>
  <div class="abs dots"><i></i><i class="on"></i><i></i></div>
</section>

<footer class="abs site-footer">
  <div class="foot-col" style="left:67px"><h6>OUR LOCATIONS</h6><ul><li>Boston</li><li>Chicago</li><li>Los Angeles</li><li>New York</li><li>Phoenix</li><li>San Francisco Bay Area</li><li>Seattle</li><li>Washington DC</li></ul></div>
  <div class="foot-col story" style="left:394px"><h6>OUR STORY</h6><ul><li>About Us</li><li>Jobs</li><li>Blog</li><li>Mobile App</li><li>Health Resources</li><li>Sitemap</li></ul></div>
  <div class="foot-col" style="left:659px"><h6>GET IN TOUCH</h6><ul><li>Help</li><li>Feedback</li><li>Media Inquiries</li><li>Where Should We Go Next?</li><li>Employer Partnerships</li><li>Practice Integration</li></ul></div>
  <div class="foot-col" style="left:985px"><h6>OUR POLICIES</h6><ul><li>Privacy Policy</li><li>HIPAA</li><li>Terms of Service</li><li>Terms of Use</li></ul></div>
</footer>
<div class="abs copyright">Copyright &copy; Global. All Rights Reserved</div>

</body>
</html>
```